Dr. Lumora needs a design for its website!

*Only need the design, coding is not required.
*Need desktop version ($500) and mobile/tablet version ($200)
*The attached files are not the exact layout we want, they are just for you to know what information should be included in those pages.
*The function of our website is like www.qavlo.hk
*For the background picture, prefer a lively picture and chinese people in it, NOT necessarily need a doctor or sick person in the picture

***Don't just copy the layout from the attachments or from the reference website, we are looking for creative ideas, non-ordinary designs!!!****

We are developing a website for the public to search a doctor by different criteria. At the initial stage, we need 4 pages to start with and other pages at later stage. I have attached the general idea of these pages but not necessarily to be exactly the same, I am looking for some new ideas.

This website needs a professional, modern, simple and user friendly design. The main color to be used in the website will be same as the color (R:0 G:139 B:205) used in our logo (see attached). We don't have any particular thoughts for the other color and the font to be used in the website. Can try to use circle outline for the icon in the navigation bar.

1. Home: will include 4 sections (see attached)

2. Doctor's details (see attached)

3. Health information: will include a short descriptions of this Health Info page and 5 sections (see attached)

4. News (see attached)

Reason: Not too many suitable designs to choose from and need more time to go through the designs

All

Medical

4 page

• must not be same as or looks too much like www.qavlo.hk
• prefer not to use black and red color

```html
<!DOCTYPE html>
<html lang="en">
<head>
<meta charset="utf-8">
<title>Dr. Lumora – Find a Doctor</title>
<link href="https://fonts.googleapis.com/css2?family=Open+Sans:wght@400;600;700;800&family=Roboto:wght@400;500&display=swap" rel="stylesheet">
<style>
:root{
  --primary:#4088cf;
  --nav:#3d87cd;
  --nav-active:#2f6ba9;
  --search:#7eb0e0;
  --panel:rgba(66,138,208,.93);
  --green:#22bb00;
  --orange:#f9a81a;
  --row-alt:#eef3f9;
  --text:#222;
  --white:#fff;
  --line:rgba(255,255,255,.3);
}
*{box-sizing:border-box;margin:0;padding:0}
html,body{width:907px;height:1200px;overflow:hidden;background:#fff;font-family:'Open Sans',sans-serif;color:var(--text)}
.page{position:relative;width:907px;height:1200px}
.abs{position:absolute}

.brand{left:100px;top:12px;display:flex;align-items:center;gap:8px}
.brand-dot{width:36px;height:36px;border-radius:50%;background:var(--primary)}
.brand-name{font-family:'Roboto',sans-serif;font-size:27px;font-weight:400;color:var(--primary)}
.lang{left:644px;top:22px;width:163px;height:34px;border:1px solid #ccc;display:flex;font-family:'Roboto',sans-serif;font-size:9.5px}
.lang span{flex:1;display:flex;align-items:center;justify-content:center;gap:5px}
.lang span+span{border-left:1px solid #ddd}
.flag{width:14px;height:9px;display:inline-block}

.nav{left:0;top:77px;width:907px;height:25px;background:var(--nav);display:flex;padding-left:99px}
.nav a{color:#fff;font-size:9.5px;font-weight:700;text-decoration:none;display:flex;align-items:center;justify-content:center;border-right:1px solid rgba(255,255,255,.25)}
.nav a.active{background:var(--nav-active)}
.nav .search{background:var(--search);color:#fff;font-size:7.5px;font-weight:700;display:flex;align-items:center;gap:6px;padding-left:12px;width:128px}

.hero-bg{left:0;top:102px;width:907px;height:431px;background:radial-gradient(ellipse at 30% 40%,#e4edf5,#c9d9e8 60%,#b6c9dc)}
.panel{left:101px;top:132px;width:706px;height:366px;background:var(--panel);box-shadow:0 2px 6px rgba(0,0,0,.12)}

.form label,.form .lbl{position:absolute;left:22px;color:#fff;font-size:9.5px;font-weight:700}
.field{position:absolute;left:22px;width:196px;height:27px;background:#fff;border:1px solid #cfd9e4}
.field svg{position:absolute;right:10px;top:9px}
.radio{position:absolute;display:flex;align-items:center;gap:8px;color:#fff;font-size:9.5px;font-weight:600}
.radio i{width:11px;height:11px;border-radius:50%;background:#fff;display:inline-block}
.btn{position:absolute;height:25px;color:#fff;font-size:9.5px;font-weight:700;display:flex;align-items:center;justify-content:center;gap:7px}

.login{left:242px;top:21px;width:223px;height:320px;border:3px solid #fff}
.login h2{position:absolute;top:35px;width:100%;text-align:center;color:#fff;font-size:15.5px;font-weight:800}
.inp{position:absolute;left:16px;width:187px;height:34px;background:#fff;border:1px solid #cfd9e4;display:flex;align-items:center;gap:9px;padding-left:14px;font-size:8.5px;color:#555}
.login-btn{position:absolute;left:16px;top:177px;width:187px;height:39px;background:var(--green);color:#fff;font-size:16px;font-weight:800;display:flex;align-items:center;justify-content:center;letter-spacing:.5px}
.forgot{position:absolute;top:254px;width:100%;text-align:center;color:#fff;font-size:9.5px;font-weight:700}

.member{left:494px;top:38px;width:182px;color:#fff;text-align:center}
.member .s{font-size:11.5px;font-weight:600}
.member .b{font-size:15px;font-weight:700;margin-top:4px}
.perks{left:494px;top:87px;width:178px;list-style:none}
.perks li{height:42.5px;display:flex;align-items:center;gap:14px;padding-left:2px;color:#fff;font-size:10px;font-weight:600;border-bottom:1px solid var(--line)}
.perks li:last-child{border-bottom:0}
.more{left:599px;top:314px;width:78px;height:27px;background:var(--orange);color:#fff;font-size:9.5px;font-weight:700;display:flex;align-items:center;justify-content:center}

.results{left:99px;top:570px;width:709px;border:1px solid #8fb6de;border-collapse:collapse;font-family:'Roboto',sans-serif;font-size:8.5px}
.results th{background:var(--primary);color:#fff;font-family:'Open Sans',sans-serif;font-weight:700;font-size:9.5px;height:30px}
.results td{text-align:center;line-height:1.42}
.results td.name,.results td.addr{text-align:left}
.results td.name{padding-left:14px}
.results tr:nth-child(even) td{background:var(--row-alt)}
.avatar{display:inline-block;width:21px;height:21px;border-radius:50%;background:var(--primary);position:relative;overflow:hidden;vertical-align:middle}

.footer{left:0;top:904px;width:907px;height:296px;background:var(--primary);color:#fff}
.col{position:absolute;top:27px}
.col h3{font-size:12px;font-weight:700;margin-bottom:11px}
.col a{display:block;color:#fff;text-decoration:none;font-family:'Roboto',sans-serif;font-size:8.2px;line-height:15.8px}
.divider{position:absolute;left:99px;top:228px;width:709px;height:1px;background:rgba(255,255,255,.3)}
.follow{position:absolute;left:99px;top:252px;display:flex;align-items:center;gap:6px;font-size:8.5px;font-weight:700}
.follow i{width:18px;height:18px;border-radius:50%;display:inline-block;background:#2f64a8}
.follow b{margin-right:6px}
.copy{position:absolute;right:99px;top:256px;font-family:'Roboto',sans-serif;font-size:8.2px}
</style>
</head>
<body>
<div class="page">

  <div class="abs brand"><span class="brand-dot"></span><span class="brand-name">Dr. Lumora</span></div>
  <div class="abs lang">
    <span><i class="flag" style="background:#1c3f8c"></i>English</span>
    <span><i class="flag" style="background:#e02020"></i>林語，中國</span>
  </div>

  <nav class="abs nav">
    <a class="active" style="width:68px">Home</a>
    <a style="width:82px">TBC</a>
    <a style="width:113px">Health Info</a>
    <a style="width:83px">News</a>
    <a style="width:102px">About Us</a>
    <a style="width:132px">Contact Us</a>
    <span class="search"><svg width="8" height="8" viewBox="0 0 10 10"><circle cx="4" cy="4" r="3" fill="none" stroke="#fff" stroke-width="1.6"/><path d="M6.3 6.3 9 9" stroke="#fff" stroke-width="1.6"/></svg>SEARCH</span>
  </nav>

  <div class="abs hero-bg" role="img" aria-label="Soft, blurred photo of smiling medical staff"></div>

  <section class="abs panel">
    <div class="form">
      <label style="top:25px">Docotr's Name</label>
      <div class="field" style="top:35px"></div>
      <span class="lbl" style="top:80px">Gender :</span>
      <span class="radio" style="left:95px;top:81px"><i></i>Male</span>
      <span class="radio" style="left:166px;top:81px"><i></i>Female</span>
      <label style="top:103px">Specialism</label>
      <div class="field" style="top:115px"><svg width="11" height="7" viewBox="0 0 11 7"><path d="M1 1l4.5 4.5L10 1" fill="none" stroke="#4088cf" stroke-width="1.5"/></svg></div>
      <label style="top:157px">Symptoms</label>
      <div class="field" style="top:169px"><svg width="11" height="7" viewBox="0 0 11 7"><path d="M1 1l4.5 4.5L10 1" fill="none" stroke="#4088cf" stroke-width="1.5"/></svg></div>
      <label style="top:211px">Distrcit</label>
      <div class="field" style="top:223px"><svg width="11" height="7" viewBox="0 0 11 7"><path d="M1 1l4.5 4.5L10 1" fill="none" stroke="#4088cf" stroke-width="1.5"/></svg></div>
      <label style="top:265px">Phone No</label>
      <div class="field" style="top:277px"></div>
      <div class="btn" style="left:22px;top:317px;width:94px;background:var(--orange)"><svg width="8" height="9" viewBox="0 0 8 9"><path d="M0 1.5h8M3 0h2M1 2.5h6l-.5 6.5h-5z" fill="#fff" stroke="#fff" stroke-width=".8"/></svg>RESET</div>
      <div class="btn" style="left:125px;top:317px;width:94px;background:var(--green)"><svg width="9" height="9" viewBox="0 0 10 10"><circle cx="4" cy="4" r="3" fill="none" stroke="#fff" stroke-width="1.6"/><path d="M6.3 6.3 9 9" stroke="#fff" stroke-width="1.6"/></svg>SEARCH</div>
    </div>

    <div class="abs login">
      <h2>MEMBER LOGIN</h2>
      <div class="inp" style="top:87px"><svg width="9" height="7" viewBox="0 0 9 7"><rect width="9" height="7" fill="#555"/><path d="M0 0l4.5 3.5L9 0" stroke="#fff" fill="none"/></svg>Login Email</div>
      <div class="inp" style="top:130px"><svg width="7" height="9" viewBox="0 0 7 9"><rect y="4" width="7" height="5" fill="#555"/><path d="M1.5 4V2.5a2 2 0 0 1 4 0V4" stroke="#555" fill="none" stroke-width="1.2"/></svg>Password</div>
      <div class="login-btn">LOGIN</div>
      <div class="forgot">Forgot Password?</div>
    </div>

    <div class="abs member"><div class="s">Become a</div><div class="b">Dr. Lumora Member</div></div>
    <ul class="abs perks">
      <li><svg width="18" height="18" viewBox="0 0 18 18" fill="none" stroke="#fff" stroke-width="1.4"><path d="M9 11 4 6a2.5 2.5 0 0 1 5-2 2.5 2.5 0 0 1 5 2z"/><path d="M1 14h5l4 2 6-3"/></svg>First Hand Health News</li>
      <li><svg width="18" height="18" viewBox="0 0 18 18" fill="#fff"><rect x="2" y="6" width="14" height="4"/><rect x="3" y="11" width="12" height="6"/><rect x="8" y="5" width="2" height="12" fill="#428ad0"/><circle cx="6.5" cy="3.5" r="2"/><circle cx="11.5" cy="3.5" r="2"/></svg>Exclusive Promotions</li>
      <li><svg width="18" height="18" viewBox="0 0 18 18" fill="none" stroke="#fff" stroke-width="1.4"><rect x="6" y="2" width="10" height="14"/><path d="M1 6l5-2v8l-5 2z" fill="#fff"/><path d="M9 7h5M9 10h5M9 13h5"/></svg>Instant Health Advices</li>
      <li><svg width="18" height="18" viewBox="0 0 18 18" fill="none" stroke="#fff" stroke-width="1.4"><path d="M1 2h16v11H8l-4 3v-3H1z"/><circle cx="6" cy="7.5" r=".6" fill="#fff"/><circle cx="9" cy="7.5" r=".6" fill="#fff"/><circle cx="12" cy="7.5" r=".6" fill="#fff"/></svg>Free Health Seminars / talks</li>
      <li><svg width="18" height="18" viewBox="0 0 18 18" fill="none" stroke="#fff" stroke-width="1.3"><rect x="1" y="3" width="16" height="13"/><path d="M1 7h16M5 1v4M13 1v4M4 10h2M8 10h2M12 10h2M4 13h2M8 13h2M12 13h2"/></svg>Priority Doctor Appointments</li>
    </ul>
    <div class="abs more">AND MORE!</div>
  </section>

  <table class="abs results">
    <thead><tr><th style="width:90px">Name</th><th style="width:60px">Gender</th><th style="width:93px">Specialism</th><th style="width:92px">林語</th><th style="width:72px">中國</th><th style="width:165px">Address</th><th style="width:62px">District</th><th>Phone No.</th></tr></thead>
    <tbody>
      <tr style="height:62px"><td class="name">Tam Ka Wing</td><td><span class="avatar"><svg width="21" height="21" viewBox="0 0 21 21"><circle cx="10.5" cy="8" r="3.6" fill="#fff"/><path d="M4 19a6.5 6 0 0 1 13 0z" fill="#fff"/></svg></span></td><td>XXXXX</td><td>Private</td><td>XXXXX</td><td class="addr">Hong Kong Harbourline Road No.<br>18 Lumen Plaza,<br>15th Floor, Room 1502-03</td><td>Kowldon</td><td>23900517</td></tr>
      <tr style="height:66px"><td class="name">Lok Wai Yan<br>Chow Mei Lin</td><td><span class="avatar"><svg width="21" height="21" viewBox="0 0 21 21"><circle cx="10.5" cy="8" r="3.6" fill="#fff"/><path d="M4 19a6.5 6 0 0 1 13 0z" fill="#fff"/></svg></span></td><td>XXXXX</td><td>Private</td><td>XXXXX</td><td class="addr">Hong Kong Harbourline Road No.<br>18 Lumen Plaza,<br>15th Floor, Room 1502-03</td><td>Kowldon</td><td>23900517</td></tr>
      <tr style="height:71px"><td class="name">Ho Chun Kit<br>Lau Siu Ming</td><td><span class="avatar"><svg width="21" height="21" viewBox="0 0 21 21"><circle cx="10.5" cy="8" r="3.6" fill="#fff"/><path d="M4 19a6.5 6 0 0 1 13 0z" fill="#fff"/></svg></span></td><td>XXXXX</td><td>Private</td><td>XXXXX</td><td class="addr">Hong Kong Harbourline Road No.<br>18 Lumen Plaza,<br>15th Floor, Room 1502-03</td><td>Kowldon</td><td>23900517</td></tr>
      <tr style="height:67px"><td class="name">Yip Hoi Tung<br>Kwan Lai Sze</td><td><span class="avatar"><svg width="21" height="21" viewBox="0 0 21 21"><circle cx="10.5" cy="8" r="3.6" fill="#fff"/><path d="M4 19a6.5 6 0 0 1 13 0z" fill="#fff"/></svg></span></td><td>XXXXX</td><td>Private</td><td>XXXXX</td><td class="addr">Hong Kong Harbourline Road No.<br>18 Lumen Plaza,<br>15th Floor, Room 1502-03</td><td>Kowldon</td><td>23900517</td></tr>
    </tbody>
  </table>

  <footer class="abs footer">
    <div class="col" style="left:99px"><h3>Popular Search</h3>
      <a>General</a><a>Obstetrics and gynecology specialist</a><a>Skin and sexually transmitted diseases specialist</a><a>ENT specialist</a><a>Orthopedic specialist</a><a>Eye specialist</a><a>Paediatrics</a><a>dentist</a><a>List of registered chiropractor</a></div>
    <div class="col" style="left:367px"><h3>Doctors Search</h3>
      <a>Search by region</a><a>Search by specialist</a><a>Comprehensive search</a><a>Doctors concentration</a><a>List of doctors</a><a>Medical card plan</a></div>
    <div class="col" style="left:578px"><h3>Health Information</h3>
      <a>Health magazine</a><a>Community News</a><a>Medical center</a><a>Medical organizations</a><a>Patient groups</a><a>Emergency Services</a></div>
    <div class="col" style="left:763px"><h3>Links</h3>
      <a>Home</a><a>TBC</a><a>Health Info</a><a>News</a><a>About Us</a><a>Contact Us</a></div>
    <div class="divider"></div>
    <div class="follow"><b>Follow us on :</b><i></i><i></i><i></i><i></i></div>
    <div class="copy">Copyrights @ 2016 All Rights Reserved</div>
  </footer>
</div>
</body>
</html>
```